Powerpoint Presentation for Farm Insurance

We recently rebranded and need to re-fresh the look of a presentation we have for customers that need insurance for their Farm. I have attached the presentation, along with our logos and style guide. In addition, some pictures are also attached., We are looking to make this a much better presentation - so we look forward to the ideas that you have that will allow us to project the great firm we are, and educate our existing and new customers on insurance related matters

```html
<!DOCTYPE html>
<html lang="en">
<head>
<meta charset="utf-8">
<title>Farm Insurance 101 – Slide Deck</title>
<link href="https://fonts.googleapis.com/css2?family=Montserrat:wght@400;600;700;800&family=Open+Sans:wght@400;600&display=swap" rel="stylesheet">
<style>
:root{
  --navy:#173766;
  --blue:#2a63ad;
  --sky:#4fa3db;
  --pale:#dcebf7;
  --gold:#f2c230;
  --ink:#28323f;
  --grey:#8a94a0;
  --paper:#ffffff;
  --bg:#eef1f4;
}
*{box-sizing:border-box;margin:0;padding:0}
html,body{width:675px;height:1200px;overflow:hidden;background:var(--bg)}
body{font-family:"Open Sans",Arial,sans-serif;color:var(--ink)}
.deck{display:grid;grid-template-columns:repeat(3,219px);grid-template-rows:repeat(6,194px);gap:5px;padding:4px 5px;width:675px;height:1200px}
.slide{position:relative;overflow:hidden;background:var(--paper);box-shadow:0 1px 3px rgba(0,0,0,.18)}
.abs{position:absolute}
.photo{position:absolute}
.h{font-family:"Montserrat",Arial,sans-serif;font-weight:800;text-transform:uppercase;letter-spacing:.3px}
.title{position:absolute;left:10px;top:8px;font-family:"Montserrat",Arial,sans-serif;font-weight:800;font-size:10px;color:var(--navy);text-transform:uppercase}
.title small{font-size:6px;font-weight:600;color:var(--grey);text-transform:none;margin-left:3px}
.rule{position:absolute;left:10px;top:22px;width:26px;height:2px;background:var(--sky)}
.tx{font-size:5px;line-height:1.45;color:var(--ink)}
.tx.w{color:#fff}
.brand{font-family:"Montserrat",Arial,sans-serif;font-weight:700;font-size:7px;letter-spacing:1px;color:#fff;display:flex;align-items:center;gap:4px}
.brand i{display:inline-block;width:7px;height:7px;background:currentColor}
.box{position:absolute;padding:4px 5px}
.circle{position:absolute;border-radius:50%}
</style>
</head>
<body>
<main class="deck">

<!-- 1 Title -->
<section class="slide">
  <div class="photo" style="inset:0;background:linear-gradient(180deg,#3a4a66 0%,#c77a3a 45%,#e9a552 58%,#3b3426 75%,#22201a 100%)" role="img" aria-label="Combine harvester in a field at sunset"></div>
  <div class="abs" style="left:0;top:10px;width:150px;height:20px;background:rgba(255,255,255,.85)"></div>
  <div class="abs h" style="left:10px;top:15px;font-size:9px;color:var(--navy)">Farm Insurance 101</div>
  <div class="abs brand" style="left:10px;bottom:10px"><i></i>HALDEN RIDGE</div>
</section>

<!-- 2 Introduction -->
<section class="slide">
  <div class="abs" style="left:0;top:0;width:219px;height:24px;background:var(--navy)"></div>
  <div class="abs h" style="left:10px;top:8px;font-size:8px;color:#fff">Introduction</div>
  <div class="abs" style="left:82px;top:14px;width:120px;height:22px;background:var(--blue)"></div>
  <div class="abs h" style="left:90px;top:17px;font-size:9px;color:#fff">Dana Merrow</div>
  <div class="abs" style="left:90px;top:29px;font-size:4.5px;color:#fff">Agriculture Risk Specialist</div>
  <div class="circle" style="left:18px;top:48px;width:34px;height:34px;background:linear-gradient(#f0b25a,#7a8a4a)" role="img" aria-label="Farm field photo"></div>
  <div class="circle" style="left:92px;top:48px;width:34px;height:34px;background:linear-gradient(#9cc3e6,#c9a24e)" role="img" aria-label="Wheat field photo"></div>
  <div class="circle" style="left:166px;top:48px;width:34px;height:34px;background:var(--navy)"></div>
  <svg class="abs" style="left:176px;top:58px" width="14" height="14" viewBox="0 0 14 14"><path d="M7 1l5 2v4c0 3-2 5-5 6-3-1-5-3-5-6V3z" fill="none" stroke="#fff" stroke-width="1.3"/><path d="M4.5 7l2 2 3-4" fill="none" stroke="#fff" stroke-width="1.3"/></svg>
  <p class="abs tx" style="left:8px;top:90px;width:60px">Twenty years helping farm families protect land, crops and livelihoods.</p>
  <p class="abs tx" style="left:80px;top:90px;width:60px">Works with growers, ranchers and dairies across the whole region.</p>
  <p class="abs tx" style="left:152px;top:90px;width:60px">Our team reviews coverage every year so nothing is missed.</p>
  <p class="abs tx" style="left:10px;top:160px;width:200px;font-style:italic;color:var(--navy)">"This presentation will focus on key farm risks and how to protect them."</p>
</section>

<!-- 3 Property -->
<section class="slide">
  <div class="title">Property</div>
  <div class="photo" style="left:0;top:28px;width:219px;height:166px;background:linear-gradient(160deg,#5a6a78,#2e3a44 60%,#1f2730)" role="img" aria-label="Farm buildings and barn"></div>
  <div class="box" style="left:90px;top:36px;width:118px;height:26px;background:var(--gold)"><div class="h" style="font-size:6px;color:var(--navy)">Lost or Damaged</div><div class="tx" style="font-size:4.5px">Buildings, stock and machinery</div></div>
  <div class="box" style="left:90px;top:68px;width:118px;height:50px;background:rgba(242,194,48,.9)"><div class="tx" style="font-size:4.5px">Barns, silos, grain bins and livestock are all exposed to fire, wind, hail and theft. Review limits each season so values keep pace with replacement costs.</div></div>
</section>

<!-- 4 Section -->
<section class="slide">
  <div class="photo" style="inset:0;background:linear-gradient(180deg,#3f6f9c,#6b9cc2 50%,#335a80)" role="img" aria-label="Blue tinted farm landscape"></div>
  <div class="abs" style="left:0;top:12px;width:62px;height:14px;background:var(--navy)"></div>
  <div class="abs" style="left:6px;top:16px;font-size:5px;color:#fff;font-family:Montserrat,sans-serif;font-weight:600">Introduction</div>
  <div class="abs" style="left:0;top:82px;width:219px;text-align:center;font-family:Montserrat,sans-serif;font-weight:600;font-size:11px;color:#fff">Why Insurance?</div>
</section>

<!-- 5 Valuation -->
<section class="slide">
  <div class="title">Valuation</div><div class="rule"></div>
  <svg class="abs" style="left:40px;top:40px" width="140" height="130" viewBox="0 0 140 130">
    <line x1="70" y1="65" x2="70" y2="14" stroke="var(--grey)" stroke-width=".8"/>
    <line x1="70" y1="65" x2="16" y2="104" stroke="var(--grey)" stroke-width=".8"/>
    <line x1="70" y1="65" x2="124" y2="104" stroke="var(--grey)" stroke-width=".8"/>
    <circle cx="70" cy="65" r="30" fill="var(--blue)"/>
    <circle cx="70" cy="14" r="6" fill="var(--sky)"/><circle cx="16" cy="104" r="6" fill="var(--sky)"/><circle cx="124" cy="104" r="6" fill="var(--sky)"/>
  </svg>
  <div class="abs h" style="left:80px;top:96px;width:60px;text-align:center;font-size:7px;color:#fff;line-height:1.2">Types of valuation</div>
  <div class="abs" style="left:86px;top:32px;font-size:5px">Actual Cash Value</div>
  <div class="abs" style="left:14px;top:152px;font-size:5px">Replacement Cost</div>
  <div class="abs" style="left:150px;top:152px;font-size:5px">Stated Amount</div>
</section>

<!-- 6 Property continued -->
<section class="slide">
  <div class="title">Property <small>(continued)</small></div>
  <div class="photo" style="left:0;top:26px;width:219px;height:40px;background:linear-gradient(90deg,#7e9a5a,#c6b06a,#8aa3b8)" role="img" aria-label="Tractor working a field"></div>
  <div class="abs h" style="left:10px;top:74px;width:100px;font-size:6px;color:var(--navy);line-height:1.3">Do you need to know all of your property?</div>
  <p class="abs tx" style="left:10px;top:98px;width:96px">• List every building and its use.<br>• Record equipment serial numbers.<br>• Track new purchases.<br>• Keep photos of key assets.<br>• Update values each renewal.</p>
  <div class="abs h" style="left:118px;top:74px;font-size:6px;color:var(--navy)">Equipment</div>
  <p class="abs tx" style="left:118px;top:86px;width:92px">Tractors, combines and tools move between fields. Scheduled coverage follows them wherever they go, on and off the farm.</p>
</section>

<!-- 7 Liability -->
<section class="slide">
  <div class="title">Liability Concerns</div>
  <div class="abs" style="left:10px;top:22px;font-size:5px;color:var(--grey)">How much is enough?</div>
  <p class="abs tx" style="left:10px;top:36px;width:200px">• The more exposure you have, the more limit you need.<br>• Liability insurance is defined as "the state of being responsible for something" by law.</p>
  <div class="box" style="left:10px;top:70px;width:62px;height:56px;border:1px solid var(--sky);background:var(--pale)"><div class="tx">Visitors on your land, farm stands and tours all create risk.</div></div>
  <div class="box" style="left:10px;top:132px;width:62px;height:50px;border:1px solid var(--sky);background:var(--pale)"><div class="tx">Livestock on roads can cause serious claims.</div></div>
  <div class="box" style="left:80px;top:70px;width:128px;height:112px;background:var(--blue)"><div class="tx w">Chemical drift, contaminated products and injured helpers can lead to lawsuits far larger than the value of the farm itself. An umbrella policy adds a layer of protection above your base limits.</div></div>
</section>

<!-- 8 Liability section -->
<section class="slide">
  <div class="photo" style="inset:0;background:linear-gradient(135deg,#6e8aa6,#2f4a66)" role="img" aria-label="Handshake over documents"></div>
  <div class="abs" style="left:0;top:118px;width:219px;height:76px;background:rgba(255,255,255,.93)"></div>
  <div class="abs h" style="left:10px;top:128px;font-size:9px;color:var(--navy)">Liability Concerns</div>
  <div class="abs" style="left:10px;top:146px;width:190px;font-family:Montserrat,sans-serif;font-size:7.5px;color:var(--blue);line-height:1.35">Is the most important piece of your insurance portfolio</div>
</section>

<!-- 9 Liability continued -->
<section class="slide">
  <div class="title">Liability Concerns <small>(continued)</small></div>
  <div class="box" style="left:10px;top:36px;width:64px;height:54px;background:var(--sky)"><div class="tx w">Is your limit high enough to cover a major claim?</div></div>
  <svg class="abs" style="left:86px;top:32px" width="122" height="106" viewBox="0 0 122 106">
    <polygon points="61,0 75,24 47,24" fill="#9fd0ef"/>
    <polygon points="45,28 77,28 90,52 32,52" fill="#6bb5e3"/>
    <polygon points="30,56 92,56 105,80 17,80" fill="var(--sky)"/>
    <polygon points="15,84 107,84 120,106 2,106" fill="var(--blue)"/>
  </svg>
  <div class="abs" style="left:126px;top:130px;font-size:5px;color:#fff;font-weight:600">$2,000,000</div>
  <p class="abs tx" style="left:10px;top:150px;width:200px">"Are you liable for something you don't do?" Courts can hold owners responsible for workers, guests and neighbours in many ways.</p>
</section>

<!-- 10 Farm Automobile -->
<section class="slide">
  <div class="photo" style="inset:0;background:linear-gradient(180deg,#9cb8c8,#6f8f4a 45%,#4a6a2e)" role="img" aria-label="Farm truck in green field"></div>
  <div class="abs" style="left:0;top:128px;width:130px;height:28px;background:rgba(42,99,173,.92)"></div>
  <div class="abs" style="left:10px;top:136px;font-family:Montserrat,sans-serif;font-weight:600;font-size:10px;color:#fff">Farm Automobile</div>
</section>

<!-- 11 Employment -->
<section class="slide">
  <div class="title">Employment Issues</div>
  <div class="photo" style="left:0;top:26px;width:219px;height:42px;background:linear-gradient(90deg,#4f6f3a,#8a9a5a,#6a7a4a)" role="img" aria-label="Workers planting crops"></div>
  <div class="abs h" style="left:10px;top:76px;font-size:7px;color:var(--navy);text-transform:none">Foreign Workers</div>
  <p class="abs tx" style="left:10px;top:88px;width:200px">• Are they covered by provincial health plans?<br>• Do you have a group health or travel benefit?<br>• Who is responsible for their transport?</p>
  <div class="abs h" style="left:10px;top:124px;font-size:7px;color:var(--navy);text-transform:none">Employee Benefits</div>
  <p class="abs tx" style="left:10px;top:136px;width:200px">• Do you offer group life and disability?<br>• Do you have key person insurance?<br>• Are seasonal staff included in your plan?</p>
</section>

<!-- 12 Emerging issues -->
<section class="slide">
  <div class="title">Emerging Issues</div>
  <div class="photo" style="left:10px;top:28px;width:60px;height:70px;background:linear-gradient(#a8c6de,#5f7d4a)" role="img" aria-label="Drone over crops"></div>
  <div class="box" style="left:78px;top:28px;width:130px;height:44px;background:var(--sky)"><div class="tx w"><b>Cyber Risk</b> – Connected equipment and online sales expose farms to hacking and data loss.</div></div>
  <div class="box" style="left:78px;top:76px;width:130px;height:44px;background:var(--blue)"><div class="tx w"><b>Climate</b> – More frequent storms, floods and drought change how crops are insured.</div></div>
  <div class="box" style="left:78px;top:124px;width:130px;height:44px;background:var(--navy)"><div class="tx w"><b>Succession</b> – Plan the transfer of the farm before the next generation takes over.</div></div>
</section>

<!-- 13 Emerging issues photos -->
<section class="slide">
  <div class="title">Emerging Issues</div>
  <div class="photo" style="left:8px;top:30px;width:46px;height:44px;background:linear-gradient(#7aa0c4,#2f4e6e)" role="img" aria-label="Solar panels"></div>
  <div class="photo" style="left:60px;top:30px;width:46px;height:44px;background:linear-gradient(#d6b47a,#8a6a3a)" role="img" aria-label="Person at a laptop"></div>
  <div class="photo" style="left:112px;top:30px;width:46px;height:44px;background:linear-gradient(#9cb87a,#4f6a3a)" role="img" aria-label="Greenhouse crops"></div>
  <div class="photo" style="left:164px;top:30px;width:46px;height:44px;background:linear-gradient(#b8c4d0,#5a6674)" role="img" aria-label="Farm machinery"></div>
  <p class="abs tx" style="left:8px;top:80px;width:46px"><b>Green Energy</b><br>Solar and wind on farms need their own coverage.</p>
  <p class="abs tx" style="left:60px;top:80px;width:46px"><b>Online Sales</b><br>Direct to customer sales add product risk.</p>
  <p class="abs tx" style="left:112px;top:80px;width:46px"><b>Agritourism</b><br>Tours and markets bring the public onto the farm.</p>
  <p class="abs tx" style="left:164px;top:80px;width:46px"><b>Contract Work</b><br>Custom work for others needs proper liability.</p>
</section>

<!-- 14 Emerging issues icons -->
<section class="slide">
  <div class="title">Emerging Issues</div>
  <svg class="abs" style="left:18px;top:34px" width="190" height="26" viewBox="0 0 190 26" fill="none" stroke="var(--blue)" stroke-width="1.5">
    <rect x="2" y="4" width="22" height="16" rx="2"/><line x1="8" y1="24" x2="18" y2="24"/>
    <circle cx="64" cy="12" r="10"/><path d="M59 12l4 4 6-8"/>
    <path d="M114 22V6l10-4 10 4v16z"/><line x1="124" y1="10" x2="124" y2="22"/>
    <path d="M164 4h20v14h-12l-6 5v-5h-2z"/>
  </svg>
  <p class="abs tx" style="left:8px;top:66px;width:46px"><b>Technology</b><br>GPS, sensors and data stored in the cloud.</p>
  <p class="abs tx" style="left:60px;top:66px;width:46px"><b>Food Safety</b><br>Recalls and contamination can be costly.</p>
  <p class="abs tx" style="left:112px;top:66px;width:46px"><b>Buildings</b><br>Large new barns raise replacement costs.</p>
  <p class="abs tx" style="left:164px;top:66px;width:46px"><b>Business</b><br>Income loss after a claim can last months.</p>
</section>

<!-- 15 P&E -->
<section class="slide">
  <div class="abs" style="left:0;top:0;width:96px;height:32px;background:var(--navy)"></div>
  <div class="abs h" style="left:8px;top:6px;font-size:6.5px;color:#fff;line-height:1.3">P &amp; E Insurance<br>Considerations</div>
  <svg class="abs" style="left:120px;top:18px" width="90" height="90" viewBox="0 0 90 90">
    <circle cx="45" cy="45" r="40" fill="none" stroke="var(--pale)" stroke-width="8"/>
    <path d="M45 5a40 40 0 0 1 38 52" fill="none" stroke="var(--sky)" stroke-width="8"/>
    <path d="M83 57a40 40 0 0 1-58 22" fill="none" stroke="var(--blue)" stroke-width="8"/>
    <circle cx="45" cy="45" r="24" fill="var(--navy)"/>
  </svg>
  <div class="abs" style="left:146px;top:58px;width:38px;text-align:center;font-size:5px;color:#fff;font-weight:600">Property &amp; Equipment</div>
  <p class="abs tx" style="left:8px;top:40px;width:104px">Building appraisals help confirm the true value of structures before a loss happens.</p>
  <div class="box" style="left:8px;top:118px;width:104px;height:66px;background:var(--navy)"><div class="tx w"><b>Working with your Representative</b><br>Meet each year to review values, changes on the farm and any new risks you have taken on.</div></div>
  <p class="abs tx" style="left:120px;top:120px;width:92px"><b>Building Appraisals</b><br>Costs to rebuild rise every year. A current appraisal keeps limits accurate and avoids shortfalls.</p>
</section>

<!-- 16 Other considerations -->
<section class="slide">
  <div class="title">Other Considerations</div>
  <svg class="abs" style="left:62px;top:30px" width="150" height="150" viewBox="0 0 150 150">
    <path d="M0 20h110v-10l20 18-20 18v-10H0z" fill="var(--sky)"/>
    <path d="M0 62h120v-10l20 18-20 18v-10H0z" fill="var(--blue)"/>
    <path d="M0 104h100v-10l20 18-20 18v-10H0z" fill="var(--navy)"/>
  </svg>
  <p class="abs tx" style="left:8px;top:40px;width:52px"><b>Life Insurance</b><br>Protect the family.</p>
  <p class="abs tx" style="left:8px;top:82px;width:52px"><b>Succession</b><br>Plan ahead.</p>
  <p class="abs tx" style="left:8px;top:124px;width:52px"><b>Critical Illness</b><br>Keep farming.</p>
  <p class="abs tx w" style="left:68px;top:54px;width:100px">Coverage for owners and partners.</p>
  <p class="abs tx w" style="left:68px;top:96px;width:100px">Tax smart transfer to children.</p>
  <p class="abs tx w" style="left:68px;top:138px;width:100px">Income while you recover.</p>
</section>

<!-- 17 Conclusion -->
<section class="slide" style="background:var(--navy)">
  <div class="abs h" style="left:10px;top:10px;font-size:9px;color:#fff">Conclusion</div>
  <div class="box" style="left:10px;top:30px;width:96px;height:110px;background:var(--blue)"><div class="tx w">Good coverage is built around your farm, not a standard form. Review property, liability, auto and people risks with your representative every year.</div></div>
  <div class="photo" style="left:114px;top:30px;width:96px;height:110px;background:linear-gradient(#4f7fb0,#24466e)" role="img" aria-label="Blue tinted field photo"></div>
  <div class="abs h" style="left:0;top:154px;width:219px;text-align:center;font-size:11px;color:#fff">Questions???</div>
</section>

<!-- 18 Thank you -->
<section class="slide">
  <div class="photo" style="left:110px;top:0;width:109px;height:194px;background:linear-gradient(180deg,#cfd8e2,#8795a6 60%,#4a5566)" role="img" aria-label="Modern office building"></div>
  <div class="abs brand" style="left:14px;top:40px;color:var(--navy);font-size:8px"><i></i>HALDEN RIDGE</div>
  <div class="abs" style="left:14px;top:84px;font-family:Montserrat,sans-serif;font-weight:600;font-size:13px;color:var(--navy)">Thank You</div>
  <div class="abs" style="left:0;top:170px;width:219px;height:24px;background:var(--navy)"></div>
  <div class="abs" style="left:14px;top:179px;font-size:5px;color:#fff">Rooted in Protection · Trusted Advisors</div>
</section>

</main>
</body>
</html>
```